SaaS / Consulting / Solution website redesign

We need a website design that:
- Is completely different than our current design : https://velmorahub.com
- Has a very minimal amount of copy
- Changes our positioning from a SaaS application to a solutions company. Solutions company means that we help our customers solve their problems with consulting, training, and tools. An example of a solutions company is here: https://pastcache.net/web/20130111103320/http://www.quintorabuild.com:80/
- Does not make us look like a start up
- Is more people oriented than technology oriented

We need a designer that:
- Is a rebel at heart
- Is a minimalist
- Tells us why our current site sucks
- Can disagree with us
- Can also do copywriting or already has a copywriter that can help
- Is ok with saying we have capability that we don't in order to see if people actually want that
- Can understand the difference between our grand vision and where we need to focus ourselves today in order to get there

Who we are:
- Entrepreneurs
- Programmers
- Consultants
- Investors

Here's our design goals:
#1 Get customers, investors, employers, and partners excited about our unique and clearly articulated value proposition
#2 Get people to contact us asking for help with their programs
#3 Position ourselves as an expert in the skills based volunteering, mentorship, and group collaboration
#4 Make it easy for people, who already know who we are, to register online

What our grand vision is:
- Create a marketplace where any person can go to our site and find time with anyone they need to meet with. Whether that is their hair stylist, school advisor, parent of your kids class, dentist, attorney, etc.

What will you get if you win:
- In addition to the prize of this project we will have many landing pages and other revisions we will need in the future. We currently don't have a designer or copywriter and need to add that capability to our team

Who do we need to appeal to:
- Directors that are launching innovative programs inside organizations
- IT personnel who are trying to disqualify our technology so they don't have to support it or deal with it when it doesn't go well
- Enterprise IT architects who don't want our product being on its own island within their organization totally incompatible with everything else. Architects which are trying to assess how our platform will co-exist with all their other platforms
- Vice Presidents who want to help their directors understand that we don't have enough experience to help them
- Program managers who have to juggle a million things and need a tool that actually helps instead of confuses them and adds more work for them.
- Program managers & directors that have been given ambiguous goals by their board of directors like "improve retention, increase engagement, create innovation, get people to collaborate." And who have no idea where to start or how to deliver on things like that.
- Program managers, directors, and vice presidents that are trying to understand how our technology and services fit into their existing technology and capability
- Employees who are bored and uninspired with their current tools and are hoping for some excitement in their life. Kind of like candy or a double espresso.
- Investors who think, our company like all the rest, are going to waste their money and make them look like a fool

Other information:
-The CSS and html needs to be responsive

-Our registration onboarding flow needs to collect this information:
User first name
user last name
user email
(verify their email)
user phone number
(verify their phone number)
User profile image (optional)
User profile summary (optional, like a bio, freeform text fiels)
If applicable: Register their organization
Organization name
Organization image (optional)
Account Mailing address
account Billing address (could be same as mailing address)
account Billing email address (could be same as user address)
account Product selection (pricing tier)
account Credit card information

The designs I am getting are a good start but they are only the front page. I just want you to know that I am expecting and need more than a landing page to complete the design. I will likely need a page that outlines the benefits and features of the product itself, how its different than our competitors, which will not be on the front page. I will need a registration flow. I will need a blog page design so we can post blog articles, I will need a team page, a page that goes into detail on our training, our services. I will likely need a page that shows all news and media we have been in. I need to show customer and user quotes, case studies, a way to contact us, partners, general resources like on collaboration, product tutorials, customers. I need the site to address a comprehensive set of needs. I need that design to be consistent and thorough. I know what LayoutBazaar is. I'm not using because I need more than a template that was customized. I need to be unique and match our brand thoughtfully, beautifully, and artistically. Someone asked me a question about how Brindle is similar to our tool in the way it is referred by end users and purchased by managers. Our website needs to primarily talk to the managers as I explained in the brief but it needs to appear cool and exciting to our end-users without focusing on the technology too much. Brindle is a tool that teams use to collaborate in small and large enterprises. The value prop for them is that communication is easier. But they don't put that on their website. Why? Because the users of the technology won't go to the website to find out information on it, they get their information from someone who is using it and demos it to them. When Nadia tells her manager Ted "Lets get brindle, Olga is using it at her company and its great" Nadia's manager doesn't know anything about brindle so she promptly googles it. The most important thing from Nadia's perspective is that Ted agrees to try it out. Ted's biggest concern is that productivity will be enhanced to degraded. Brindle knows this and so on the front page they know they are talking to Ted NOT Nadia because Nadia is already sold on it and doesn't need to get sold on the website. Nadia is end user. Ted is the purchaser. We have the same problem and so our end users are not the ones purchasing our product, their managers are purchasing our product. We get referred by our end users and vetted by their managers. Hope this helps! Thank you for looking at this project!  Added Wednesday, June 7, 2017

Another observation I am having about the designs being submitted. I believe we used the animations on our current website because animations / cartoons connect with the "inner child" in our users. Whatever that means :-). I think it's what makes our brand fun. I have a hard time imagining that we could make the design fun looking without animations but I'm sure it can be achieved. I also recognize that blending pictures of real people and animations is hard. So either we must masterfully blend them, use only animations, or make the real people have a LOT of fun! So far most of the designs while achieve the goal of appealing to the serious Vice Presidents and directors, they are not doing a good job at appealing to the overworked program managers and bored employees. There seems to stand another challenge with animations which is animations are hard to find and/or create that achieve the message / emotion we are trying to communicate. I don't have any good answers for this but I will say we can hire both animators and illustrators if we need to. All you have to do is communicate the effect in the website design with some simpler version maybe not the end illustration or animation itself. Added Wednesday, June 7, 2017

Industry/Entity Type

Saas

Coding

Coded - Design and coding required

Number of Pages Required

5+ page

Font styles to use
Sans Serif

Requirements
Must have
• Sex appeal and a sense of humor. Copy that makes people excited and clairvoyant about our potential.
Should not have
• Boring renditions of other non-inspiring websites

```html
<!DOCTYPE html>
<html lang="en">
<head>
<meta charset="utf-8">
<title>Velmora — Solutions for people-powered programs</title>
<link rel="stylesheet" href="https://fonts.googleapis.com/css2?family=Montserrat:wght@400;600;700&family=Open+Sans:wght@400;600&display=swap">
<style>
:root{
  --slate:#5f7b8a;
  --slate-dark:#4f6877;
  --slate-text:#5a7484;
  --yellow:#fbdc5c;
  --yellow-soft:#fde98f;
  --cream:#fdf4cf;
  --white:#ffffff;
  --field:#f2f2f2;
  --ink:#555f66;
  --footer:#2f2f2f;
  --footer-bar:#232323;
}
*{box-sizing:border-box;margin:0;padding:0}
html,body{width:1200px;height:2799px;overflow:hidden}
body{position:relative;background:var(--white);font-family:"Open Sans",Arial,sans-serif;color:var(--ink)}
.abs{position:absolute}
.heading{font-family:"Montserrat",Arial,sans-serif;font-weight:700;letter-spacing:1px}

/* hero */
.hero{left:0;top:0;width:1200px;height:1210px;background:linear-gradient(160deg,#6a8594 0%,var(--slate) 45%,#5c7886 100%)}
.brand{left:250px;top:46px;display:flex;align-items:center;gap:9px;color:var(--white);font-family:"Montserrat",Arial,sans-serif;font-weight:600;font-size:26px;line-height:1;white-space:nowrap}
.brand-dot{width:28px;height:28px;border-radius:50%;border:3px solid var(--white);flex:none}
.top-link{top:17px;font-size:9px;color:var(--white);white-space:nowrap;line-height:14px}
.pill-outline{border:1.5px solid var(--yellow);border-radius:12px;padding:3px 14px;font-weight:600}
.nav-item{top:70px;font-size:10px;color:var(--white);white-space:nowrap;line-height:14px}
.nav-item.active{border-bottom:2px solid var(--yellow);padding-bottom:5px}
.btn-login{left:879px;top:64px;width:72px;height:23px;border-radius:12px;background:var(--yellow);color:#333;font-size:10px;font-weight:600;display:flex;align-items:center;justify-content:center}
.hero-photo{left:414px;top:136px;width:540px;height:554px;border-radius:50% 0 50% 50%;background:linear-gradient(135deg,#eef2f5 0%,#c9d4dc 55%,#8ea2b0 100%);border:3px solid var(--white)}
.bubble{left:246px;top:202px;width:250px;height:250px;border-radius:50% 50% 0 50%;background:var(--yellow);text-align:center;border:3px solid var(--white)}
.bubble-title{position:absolute;left:0;right:0;top:30px;font-size:21px;line-height:24px;color:var(--slate-dark);font-family:"Open Sans",Arial,sans-serif}
.bubble-screen{position:absolute;left:32px;top:176px;width:166px;height:102px;background:linear-gradient(180deg,#ffffff,#e6edf1);border-radius:4px}
.bubble-btn{position:absolute;left:102px;top:162px;width:92px;height:22px;border-radius:11px;background:var(--slate);color:var(--white);font-size:9px;font-weight:600;display:flex;align-items:center;justify-content:center;z-index:2}
.dots{left:327px;top:598px;display:flex;gap:9px}
.dots span{width:9px;height:9px;border-radius:50%;background:rgba(255,255,255,.55)}
.dots span:first-child{background:var(--white)}

/* who we are */
.who-title{left:0;width:1200px;top:745px;text-align:center;color:var(--white);font-size:28px}
.who-text{left:290px;width:620px;top:806px;text-align:center;color:var(--white);font-size:12px;line-height:20px}
.divider{left:540px;top:898px;width:120px;height:3px;background:linear-gradient(90deg,var(--yellow) 50%,var(--white) 50%)}
.role{top:940px;width:200px;text-align:center;color:var(--white)}
.role svg{display:block;margin:0 auto 14px}
.role h3{font-weight:400;font-size:15px;margin-bottom:10px}
.role p{font-size:10px;line-height:15px;padding:0 8px}

/* marketplace */
.market-bg{left:0;top:1180px;width:1200px;height:760px}
.market-title{left:0;width:1200px;top:1318px;text-align:center;color:var(--white);font-size:28px}
.card{top:1401px;width:196px;text-align:center}
.card-img{width:196px;height:196px;border:3px solid var(--white)}
.card h3{font-family:"Montserrat",Arial,sans-serif;font-size:14px;color:var(--white);margin:18px 0 8px}
.card p{font-size:10px;line-height:15px;color:var(--white)}
.btn-more{margin:16px auto 0;width:92px;height:24px;border-radius:12px;background:var(--slate);color:var(--white);font-size:9px;font-weight:600;display:flex;align-items:center;justify-content:center}
.arrow{width:28px;height:28px;border-radius:50%;background:var(--white);top:1484px;display:flex;align-items:center;justify-content:center}

/* contact */
.contact-title{left:0;width:1200px;top:1912px;text-align:center;color:var(--slate-text);font-size:30px}
.info{top:2016px;width:220px;text-align:center}
.info svg{display:block;margin:0 auto 10px}
.info h4{font-family:"Montserrat",Arial,sans-serif;font-size:10px;color:#444;letter-spacing:1px;margin-bottom:4px}
.info p{font-size:10px;line-height:15px;color:#777}
.vline{top:1989px;width:1px;height:134px;background:#e4e4e4}
.ask{left:0;width:1200px;top:2166px;text-align:center;color:var(--slate-text);font-size:14px;line-height:21px;letter-spacing:1.5px}
.field{left:248px;width:706px;height:34px;background:var(--field);font-size:10px;color:#999;padding:10px 12px}
.field.area{height:123px}
.btn-send{left:527px;top:2549px;width:147px;height:35px;border-radius:18px;background:var(--yellow);box-shadow:0 3px 0 #e3c44a;color:#333;font-size:13px;font-weight:600;display:flex;align-items:center;justify-content:center}

/* footer */
.footer{left:0;top:2635px;width:1200px;height:121px;background:var(--footer)}
.footer .brand{left:250px;top:46px;font-size:20px;gap:7px}
.footer .brand-dot{width:22px;height:22px;border-width:2.5px}
.foot-col{top:34px;font-size:10px;line-height:16px;color:var(--white);font-weight:600;white-space:nowrap}
.foot-bar{left:0;top:2756px;width:1200px;height:43px;background:var(--footer-bar)}
.copy{left:248px;top:15px;font-size:9px;color:#aaa}
.copy b{color:var(--yellow);font-weight:600}
.social{left:582px;top:14px;display:flex;gap:24px}
.social span{width:13px;height:13px;border-radius:50%;background:var(--white)}
</style>
</head>
<body>

<section class="hero abs">
  <div class="brand abs"><span class="brand-dot"></span>Velmora</div>
  <span class="top-link pill-outline abs" style="left:776px;top:15px">Free Trials</span>
  <span class="top-link abs" style="left:862px">&#9679; Sign In</span>
  <span class="top-link abs" style="left:912px">&#9675; Search</span>
  <nav>
    <span class="nav-item active abs" style="left:494px">Products</span>
    <span class="nav-item abs" style="left:560px">Solutions</span>
    <span class="nav-item abs" style="left:631px">Services &amp; Support</span>
    <span class="nav-item abs" style="left:741px">Partners</span>
    <span class="nav-item abs" style="left:806px">Company</span>
  </nav>
  <div class="btn-login abs">Login</div>

  <div class="hero-photo abs" role="img" aria-label="Photo of two smiling colleagues working together at a laptop in a bright office"></div>
  <div class="bubble abs">
    <p class="bubble-title">Increase<br>face-to-face<br>engagement in your<br>communities and<br>groups</p>
    <div class="bubble-btn">Schedule Demo</div>
    <div class="bubble-screen" role="img" aria-label="Screenshot of the Velmora dashboard with a bar chart"></div>
  </div>
  <div class="dots abs"><span></span><span></span><span></span><span></span></div>

  <h2 class="who-title heading abs">WHO WE ARE</h2>
  <p class="who-text abs">Lorem Ipsum is simply dummy text of the printing and typesetting industry. Lorem Ipsum has been the industry's standard dummy text ever since the 1500s, when an unknown printer took a galley of type and scrambled it to make a type specimen book.</p>
  <div class="divider abs"></div>

  <div class="role abs" style="left:169px">
    <svg width="56" height="62" viewBox="0 0 56 62"><circle cx="28" cy="24" r="20" fill="var(--yellow)"/><rect x="19" y="42" width="18" height="12" rx="2" fill="var(--yellow)"/><rect x="22" y="55" width="12" height="5" rx="2" fill="#e8c94a"/><path d="M24 40v-12l4-4 4 4v12" stroke="#fff" stroke-width="2" fill="none"/></svg>
    <h3>Entrepreneurs</h3>
    <p>Lorem Ipsum has been the industry's standard dummy text ever since the 1500s, when an unknown printer took a galley of type and scrambled it to make a type specimen book.</p>
  </div>
  <div class="role abs" style="left:387px">
    <svg width="62" height="62" viewBox="0 0 62 62"><path d="M30 4c15 0 24 10 24 22 0 5-2 8-2 11l6 9-6 2v6c0 3-2 4-5 4h-6v4H14v-12C8 45 5 37 5 28 5 14 16 4 30 4z" fill="var(--yellow)"/><path d="M30 4C16 4 5 14 5 28c0 9 3 17 9 22v12h16z" fill="#f3cd3d"/><text x="16" y="26" font-family="Montserrat,sans-serif" font-size="9" font-weight="700" fill="#fff">0110</text><text x="16" y="37" font-family="Montserrat,sans-serif" font-size="9" font-weight="700" fill="#fff">0101</text></svg>
    <h3>Programmers</h3>
    <p>Lorem Ipsum is simply dummy text of the printing and typesetting industry</p>
  </div>
  <div class="role abs" style="left:609px">
    <svg width="80" height="62" viewBox="0 0 80 62"><rect x="4" y="18" width="32" height="26" rx="2" fill="var(--yellow)"/><rect x="30" y="2" width="32" height="26" rx="2" fill="var(--yellow)"/><rect x="44" y="30" width="32" height="26" rx="2" fill="var(--yellow)"/><path d="M12 44l0 8 8-8zM54 28l0 6 6-6zM66 56l0 6-8-6z" fill="var(--yellow)"/><circle cx="20" cy="28" r="4" fill="#fff"/><circle cx="46" cy="12" r="4" fill="#fff"/><circle cx="60" cy="40" r="4" fill="#fff"/></svg>
    <h3>Consultants</h3>
    <p>It has survived not only five centuries, but also the leap into electronic typesetting, remaining essentially unchanged</p>
  </div>
  <div class="role abs" style="left:827px">
    <svg width="72" height="62" viewBox="0 0 72 62"><rect x="4" y="6" width="60" height="40" rx="2" fill="var(--yellow)"/><rect x="10" y="12" width="48" height="28" fill="none" stroke="#fff" stroke-width="2"/><circle cx="50" cy="44" r="10" fill="#f3cd3d"/><path d="M44 52l-3 9 9-4 9 4-3-9" fill="#f3cd3d"/><rect x="16" y="20" width="24" height="3" fill="#fff"/><rect x="16" y="27" width="18" height="3" fill="#fff"/></svg>
    <h3>Investors</h3>
    <p>It was popularised in the 1960s with the release of Tessaline sheets containing Lorem Ipsum passages, and more recently with desktop publishing software like Quillset Composer of Lorem Ipsum.</p>
  </div>
</section>

<svg class="market-bg abs" viewBox="0 0 1200 760" preserveAspectRatio="none">
  <defs>
    <linearGradient id="marketFade" x1="0" x2="1" y1="0" y2="0">
      <stop offset="0" stop-color="#fbdc5c" stop-opacity="0"/>
      <stop offset="1" stop-color="#d9c9a0" stop-opacity="0.85"/>
    </linearGradient>
  </defs>
  <polygon points="0,24 597,95 0,167" fill="var(--cream)"/>
  <polygon points="0,167 597,95 1200,24 1200,710 0,560" fill="var(--yellow)"/>
  <polygon points="0,560 597,686 0,752" fill="var(--cream)"/>
  <polygon points="760,60 1200,24 1200,710 760,640" fill="url(#marketFade)" role="img" aria-label="Soft photo of a smiling professional woman fading into the yellow band"/>
</svg>

<h2 class="market-title heading abs">MARKETPLACE</h2>
<div class="arrow abs" style="left:184px"><svg width="10" height="10" viewBox="0 0 10 10"><path d="M7 1L3 5l4 4" stroke="var(--yellow)" stroke-width="2" fill="none"/></svg></div>
<div class="arrow abs" style="left:986px"><svg width="10" height="10" viewBox="0 0 10 10"><path d="M3 1l4 4-4 4" stroke="var(--yellow)" stroke-width="2" fill="none"/></svg></div>

<article class="card abs" style="left:250px">
  <div class="card-img" role="img" aria-label="Photo of a judge's gavel" style="background:linear-gradient(135deg,#c9a77f,#6b3b26)"></div>
  <h3>Attorney</h3>
  <p>Lorem Ipsum has been the industry's standard dummy text ever since the 1500s, when an unknown printer took a galley of type and scrambled it to make a type specimen book.</p>
  <div class="btn-more">Learn More</div>
</article>
<article class="card abs" style="left:502px">
  <div class="card-img" role="img" aria-label="Photo of schoolchildren drawing at a classroom table" style="background:linear-gradient(135deg,#e6dccf,#6f8fc4)"></div>
  <h3>School Advisor</h3>
  <p>Lorem Ipsum has been the industry's standard dummy text ever since the 1500s, when an unknown printer took a galley of type and scrambled it to make a type specimen book.</p>
  <div class="btn-more">Learn More</div>
</article>
<article class="card abs" style="left:756px">
  <div class="card-img" role="img" aria-label="Photo of a patient smiling during a dental check-up" style="background:linear-gradient(135deg,#f1d3c4,#7fb6d6)"></div>
  <h3>Dentist</h3>
  <p>Lorem Ipsum has been the industry's standard dummy text ever since the 1500s, when an unknown printer took a galley of type and scrambled it to make a type specimen book.</p>
  <div class="btn-more">Learn More</div>
</article>

<h2 class="contact-title heading abs">CONTACT US</h2>
<div class="vline abs" style="left:483px"></div>
<div class="vline abs" style="left:717px"></div>
<div class="info abs" style="left:258px">
  <svg width="14" height="22" viewBox="0 0 14 22"><rect x="1" y="1" width="12" height="20" rx="2" fill="none" stroke="var(--slate-text)" stroke-width="1.6"/><circle cx="7" cy="17" r="1.3" fill="var(--slate-text)"/></svg>
  <h4>PHONE</h4>
  <p>Phone 1: +0 000 000 0000<br>Phone 2: +0 000 000 0000</p>
</div>
<div class="info abs" style="left:491px">
  <svg width="18" height="22" viewBox="0 0 18 22"><path d="M9 21s7-7.5 7-12.5A7 7 0 0 0 2 8.5C2 13.5 9 21 9 21z" fill="none" stroke="var(--slate-text)" stroke-width="1.6"/><circle cx="9" cy="8.5" r="2.5" fill="none" stroke="var(--slate-text)" stroke-width="1.6"/></svg>
  <h4>ADDRESS</h4>
  <p>ABC, Street City, Coounty</p>
</div>
<div class="info abs" style="left:728px">
  <svg width="24" height="18" viewBox="0 0 24 18"><rect x="1" y="1" width="22" height="16" fill="none" stroke="var(--slate-text)" stroke-width="1.6"/><path d="M1 1l11 9 11-9" fill="none" stroke="var(--slate-text)" stroke-width="1.6"/></svg>
  <h4>EMAIL</h4>
  <p>support@velmorahub.com<br>hello@velmorahub.com</p>
</div>

<p class="ask heading abs">IF YOU GOT ANY QUESTIONS<br>PLEASE DO NOT HESITATE TO SEND US A MESSAGE.</p>
<div class="field abs" style="top:2249px">Your Name</div>
<div class="field abs" style="top:2299px">Your Email</div>
<div class="field abs" style="top:2348px">Subject</div>
<div class="field area abs" style="top:2396px">Message</div>
<div class="btn-send abs">Send Message</div>

<footer class="footer abs">
  <div class="brand abs"><span class="brand-dot"></span>Velmora</div>
  <div class="foot-col abs" style="left:394px">Products<br>Solutions<br>Free Trials</div>
  <div class="foot-col abs" style="left:498px">Education &amp; Training<br>Services &amp; Support<br>Communities<br>Velmora for Developers</div>
  <div class="foot-col abs" style="left:680px">About Us<br>Careers<br>Newsroom<br>Executive Management</div>
  <div class="foot-col abs" style="left:831px">Contact Us<br>Velmora<br>Velmora Highlight Blog</div>
</footer>
<div class="foot-bar abs">
  <p class="copy abs">Copyrights © 2017 by <b>Velmora</b>. All Rights Reserved.</p>
  <div class="social abs"><span></span><span></span><span></span><span></span></div>
</div>

</body>
</html>
```